Need Brochure Design For Pizza Restaurant

Need redesign for pizza restaurant. Brochure size is 11 Inches X 17 Inches Roll Fold.

Specifications and original menu will be attached.

Target Market(s)

Those who enjoy Pizza ;)

Industry/Entity Type

Restaurant

Requirements
Must have
• The brochure must be double sided.

Must include important information such as operating hours, telephone number, etc.

The brochure should have a snapshot of a map such as Rovi Charts showing the location of the establishment.

All these information could be found on our Rovi Spots page:
http://charts.rovimapex.ca/charts?hl=en&sugexp=frgbld&gs_nf=1&pq=tz+pizza&cp=9&gs_id=4&xhr=t&q=tz%20pizza%20fort%20mcmurray&bav=on.2,or.r_gc.r_pw.r_qf.,cf.osb&biw=1584&bih=810&um=1&ie=UTF-8&sa=N&tab=il

There should be a place where the receiver can cut out a piece of the menu to get a coupon, like in the original design I attached, in which case, there should not be anything important on the reverse side of the brochure where the cut out is to be made.

Final copy needs to be in PDF and PSD, the latter must be separated into layers for ease of later editing.
Nice to have
• Highlight the importance that the establishment is under new management and recently renovated.

```html
<!DOCTYPE html>
<html lang="en">
<head>
<meta charset="utf-8">
<title>TZ's Pizza Menu Brochure – Inside Spread</title>
<link rel="stylesheet" href="https://fonts.googleapis.com/css2?family=Archivo+Black&family=Arimo:wght@400;700&display=swap">
<style>
:root{
  --red:#c3141c;
  --red-deep:#9c0c12;
  --red-light:#d8262b;
  --ink:#ffffff;
  --outline:#1a0506;
  --paper:#ffffff;
  --label:#2b2b2b;
  --leaf:#b8612a;
  --cream:#e9d6a6;
}
*{margin:0;padding:0;box-sizing:border-box}
html,body{width:1200px;height:900px;overflow:hidden;background:var(--paper)}
body{position:relative;font-family:"Arimo",Arial,sans-serif;color:var(--ink)}
.spread{position:absolute;left:0;top:0;width:1200px;height:778px;
  background:radial-gradient(ellipse at 50% 45%,var(--red-light) 0%,var(--red) 45%,var(--red-deep) 100%);overflow:hidden}
.panel{position:absolute;top:0;height:778px}
.panel--left{left:6px;width:334px}
.panel--middle{left:376px;width:416px}
.panel--right{left:806px;width:388px}
.title{font-family:"Archivo Black",Arial,sans-serif;font-size:20px;text-align:center;color:var(--ink);
  text-shadow:1px 1px 0 var(--outline),-1px -1px 0 var(--outline),1px -1px 0 var(--outline),-1px 1px 0 var(--outline);line-height:24px}
.name{font-weight:700;color:var(--ink);
  text-shadow:1px 1px 0 var(--outline),-.5px -.5px 0 var(--outline),.5px -.5px 0 var(--outline),-.5px .5px 0 var(--outline)}
.row{display:flex;align-items:flex-end;font-weight:700}
.row .text{flex:0 1 auto}
.row .lead{flex:1 1 6px;min-width:6px;border-bottom:1px dotted rgba(255,255,255,.85);margin:0 1px 2px}
.row .price{flex:0 0 auto;white-space:nowrap}
.panel--left{font-size:8.2px;line-height:9.6px}
.panel--left .title{margin-top:2px;line-height:22px}
.panel--left .price{word-spacing:2px}
.sizes{display:flex;justify-content:flex-end;font-weight:700;font-size:9px;padding-right:8px;gap:14px;margin-top:-11px;margin-bottom:1px}
.bullets .row .text::before{content:"• "}
.toppings{display:grid;grid-template-columns:104px 1fr;font-weight:700}
.note{font-weight:700}
.spacer{height:5px}
.title--sub{font-size:17px;line-height:18px!important;margin-top:0!important}
.title--foot{font-size:17px;line-height:19px!important;margin-top:4px!important}
.panel--middle{font-size:9.4px;line-height:12.4px;padding:0 2px}
.panel--middle .title{margin:8px 0 4px;font-size:21px}
.panel--right{font-size:9px;line-height:10.4px}
.panel--right .title{margin:8px 0 2px;font-size:21px}
.panel--right .subtitle{font-family:"Archivo Black",Arial,sans-serif;font-size:15px;text-align:center;line-height:20px;
  text-shadow:1px 1px 0 var(--outline),-1px -1px 0 var(--outline),1px -1px 0 var(--outline),-1px 1px 0 var(--outline)}
.panel--right .gap{height:9px}
.art{position:absolute}
.art--leaves{left:344px;top:120px;width:24px;height:600px;background:linear-gradient(180deg,rgba(233,214,166,.25),rgba(184,97,42,.3),rgba(233,214,166,.2))}
.art--pepper{left:530px;top:365px;width:100px;height:105px;border-radius:50%;
  background:radial-gradient(circle,rgba(90,140,40,.5),rgba(90,140,40,0) 70%)}
.art--food{left:870px;top:712px;width:330px;height:66px;
  background:linear-gradient(90deg,rgba(233,214,166,0),rgba(233,214,166,.5) 30%,rgba(200,120,60,.55) 65%,rgba(233,214,166,.45))}
.labels{position:absolute;top:812px;left:0;width:1200px;height:34px;font-family:"Arimo",Arial,sans-serif;font-size:27px;color:var(--label)}
.labels span{position:absolute;top:0}
</style>
</head>
<body>
<main class="spread">
  <div class="art art--leaves" role="img" aria-label="Decorative autumn leaves and chili peppers"></div>
  <div class="art art--pepper" role="img" aria-label="Green jalapeño pepper illustration"></div>
  <div class="art art--food" role="img" aria-label="Soft drink cans and pizzas"></div>

  <section class="panel panel--left">
    <h2 class="title">2 For 1 Pastas</h2>
    <div class="sizes"><span>10"</span><span>12"</span><span>14"</span></div>
    <div class="row"><span class="text">Cheese</span><i class="lead"></i><span class="price">$19.95 $23.95 $29.95</span></div>
    <div class="row"><span class="text">Pepperoni</span><i class="lead"></i><span class="price">$21.95 $25.95 $31.95</span></div>
    <div class="row"><span class="text">Pepperoni &amp; Mushroom</span><i class="lead"></i><span class="price">$22.95 $26.95 $32.95</span></div>
    <div class="row"><span class="text">Hawaiian</span><i class="lead"></i><span class="price">$24.95 $28.95 $34.95</span></div>
    <div class="name">Double Bacon</div>
    <div class="row"><span class="text">Bacon and Back Bacon</span><i class="lead"></i><span class="price">$24.95 $28.95 $35.95</span></div>
    <div class="name">Canuck</div>
    <div class="row"><span class="text">Pepperoni, Ham and Back Bacon</span><i class="lead"></i><span class="price">$25.95 $29.95 $36.95</span></div>
    <div class="name">All Dressed</div>
    <div class="row"><span class="text">Pepperoni, Mushroom, Onion and Green Pepper</span><i class="lead"></i><span class="price">$25.95 $29.95 $36.95</span></div>
    <div class="name">Meat Lovers</div>
    <div class="row"><span class="text">Pepperoni, Ground Beef, Ham and Back Bacon</span><i class="lead"></i><span class="price">$26.95 $30.95 $37.95</span></div>
    <div class="name">Greek</div>
    <div class="row"><span class="text">Black Olive, Onions, Green Peppers, Feta and Tomatoes</span><i class="lead"></i><span class="price">$24.95 $28.95 $35.95</span></div>
    <div class="name">Vegetarian</div>
    <div class="row"><span class="text">Black Olives, Onions, Green Peppers, Mushrooms and Tomatoes</span><i class="lead"></i><span class="price">$24.95 $29.95 $36.95</span></div>
    <div class="name">Mexican</div>
    <div class="row"><span class="text">Salsa, Beef, Onion, Green Pepper, Cheddar and Mozza</span><i class="lead"></i><span class="price">$25.95 $29.95 $36.95</span></div>
    <div class="name">Donair</div>
    <div class="row"><span class="text">Donair, Onion, Tomatoes and Sweet Sauce</span><i class="lead"></i><span class="price">$25.95 $29.95 $36.95</span></div>
    <div class="name">Fire Chicken</div>
    <div class="row"><span class="text">Salsa, Chicken, Onions and Hot Peppers</span><i class="lead"></i><span class="price">$25.95 $29.95 $36.95</span></div>
    <div class="name">Classic Italian</div>
    <div class="row"><span class="text">Cappacolo, Pepperoni, Green Pepper, Salami and Olives</span><i class="lead"></i><span class="price">$25.95 $29.95 $36.95</span></div>
    <div class="name">BBQ Chicken</div>
    <div class="row"><span class="text">BBQ Sauce, Chicken, Green Peppers and Tomato</span><i class="lead"></i><span class="price">$25.95 $29.95 $36.95</span></div>
    <div class="name">Cheese Burger</div>
    <div class="row"><span class="text">Beef, Mushroom, Onions, Bacon, Cheddar and Mozza</span><i class="lead"></i><span class="price">$26.95 $30.95 $37.95</span></div>
    <div class="name">TZ's Special</div>
    <div class="row"><span class="text">Pepperoni, Mushrooms, Ham, Italian Sausage, Green Pepper and Tomatoes</span><i class="lead"></i><span class="price">$28.95 $32.95 $39.95</span></div>
    <div class="row"><span class="text">Garlic Cheese Fingers</span><i class="lead"></i><span class="price">$20.95 $24.95 $29.95</span></div>
    <div class="name">Create Your Own</div>
    <div class="bullets">
      <div class="row"><span class="text">One Topping</span><i class="lead"></i><span class="price">$20.95 $24.95 $31.95</span></div>
      <div class="row"><span class="text">Two Toppings</span><i class="lead"></i><span class="price">$23.95 $27.95 $34.95</span></div>
      <div class="row"><span class="text">Three Toppings</span><i class="lead"></i><span class="price">$24.95 $28.95 $35.95</span></div>
      <div class="row"><span class="text">Four Toppings</span><i class="lead"></i><span class="price">$25.95 $29.95 $36.95</span></div>
      <div class="row"><span class="text">Five Toppings</span><i class="lead"></i><span class="price">$26.95 $30.95 $37.95</span></div>
    </div>
    <div class="note">* Cheeses don't count as toppings.</div>
    <div class="spacer"></div>
    <div class="row"><span class="text">1 Pizza Only...Up To Four Toppings</span><i class="lead"></i><span class="price">$14.95 $19.95 $24.95</span></div>
    <div class="row"><span class="text">Extra toppings</span><i class="lead"></i><span class="price">$2.50 $3.00 &nbsp; $3.50</span></div>
    <div class="toppings">
      <span>Meat Toppings..........</span><span>Chicken, Pepperoni, Bacon, Back Bacon, Salami, Ham, Ground Beef, Italian Sausage, Cappacolo and Baby Shrimp.</span>
      <span>Vegetable Toppings...</span><span>Onions, Mushrooms, Tomatoes, Green Peppers, Hot Peppers, Jalapeno, Black Olives, Salsa, Pineapple, Cooked Tomatoes, Extra Cheese, Extra Sauce.</span>
      <span>Cheeses....................</span><span>Cheese Mozzarella, Cheddar, Feta and Parmesan.</span>
    </div>
    <div class="row"><span class="text">Dipping Sauces............ Sweet Sauce</span><i class="lead"></i><span class="price">$1.50</span></div>
    <h2 class="title title--sub">Pastas</h2>
    <div class="name">Chicken Mushroom Fettuccini</div>
    <div class="row"><span class="text">Pasta covered in creamy white wine sauce with bacon bits, grilled chicken and mushrooms</span><i class="lead"></i><span class="price">$14.95</span></div>
    <div class="name">Shrimp Fettuccini</div>
    <div class="row"><span class="text">Pasta covered in creamy white wine sauce with grilled shrimp</span><i class="lead"></i><span class="price">$14.95</span></div>
    <div class="name">Montreal Steak Bowl</div>
    <div class="row"><span class="text">Fettuccini topped with sautéed peppers, onions, mushrooms all mixed together with Montreal Steak Spices and topped with a flame grilled 6 oz. steak</span><i class="lead"></i><span class="price">$16.95</span></div>
    <div class="name">Lasagna</div>
    <div class="row"><span class="text">Layers of pasta and meat sauce baked with lots of mozzarella cheese</span><i class="lead"></i><span class="price">$11.95</span></div>
    <div class="name">Traditional Spaghetti</div>
    <div class="row"><span class="text">Spaghetti topped with our hearty homemade meat sauce</span><i class="lead"></i><span class="price">$11.95</span></div>
    <div class="name">Baked Spaghetti</div>
    <div class="row"><span class="text">Spaghetti topped with meat sauce and cheese baked fresh from the oven</span><i class="lead"></i><span class="price">$12.95</span></div>
    <div class="name">Cajun Deluxe Penne</div>
    <div class="row"><span class="text">Chicken, shrimp, onions, peppers, Italian sausages and tomato sauce finished in Cajun seasoning. This is a spicy one</span><i class="lead"></i><span class="price">$14.95</span></div>
    <div class="name">Meatballs</div>
    <div class="row"><span class="text">Three tasty meatballs</span><i class="lead"></i><span class="price">$1.60</span></div>
    <h2 class="title title--foot">2 For 1 Pastas</h2>
    <div class="row"><span class="text">2 For 1 Traditional Pasta, Lasagna, or Fettuccini &amp; Alfredo Sauce</span><i class="lead"></i><span class="price">$18.95</span></div>
    <div class="row"><span class="text">2 For 1 Baked Pasta, Lasagna, or Fettuccini &amp; Alfredo Sauce</span><i class="lead"></i><span class="price">$20.95</span></div>
  </section>

  <section class="panel panel--middle">
    <h2 class="title">Appetizers</h2>
    <div class="name">TZ's Chicken Wings</div>
    <div class="row"><span class="text">A dozen classic chicken wings deep fried to a golden crisp and can be flavored: Teriyaki, BBQ, Hot, Mild, Salt &amp; Pepper, Golden, Honey Garlic, Thai Chili or Lemon Pepper</span><i class="lead"></i><span class="price">$9.95</span></div>
    <div class="name">Chubby Chicken Wings</div>
    <div class="row"><span class="text">They are the biggest, juiciest, and meatiest dozen wings you have ever seen. They can be flavored: Teriyaki, BBQ, Hot, Mild, Salt &amp; Pepper, Golden, Honey Garlic, Thai Chili or Lemon Pepper</span><i class="lead"></i><span class="price">$11.95</span></div>
    <div class="name">TZ's Platter</div>
    <div class="row"><span class="text">Four golden chicken wings, two chicken fingers, two mozza sticks, two jalapeno poppers, two mini beef tacos, two torpedo shrimps and sweet potato fries served with celery sticks, carrot sticks, ranch dressing, plum sauce and salsa</span><i class="lead"></i><span class="price">$14.95</span></div>
    <div class="name">Sweet Potato Wedges</div>
    <div class="row"><span class="text">8 oz. of deep fried sweet potato fries. This delicious snack is an instant TZ's Classic</span><i class="lead"></i><span class="price">$6.95</span></div>
    <div class="name">Nachos</div>
    <div class="row"><span class="text">Nacho chips topped with cheese, green onions, jalapeno peppers, and tomatoes. Served with sour cream and salsa. Add chicken or beef for</span><i class="lead"></i><span class="price">$11.95</span></div>
    <div class="name">Boneless Garlic Ribs</div>
    <div class="row"><span class="text">8 oz. of garlic ribs sprinkled with Montreal Steak Seasoning and served with plum sauce</span><i class="lead"></i><span class="price">$8.95</span></div>
    <div class="name">Jalapeno Poppers</div>
    <div class="row"><span class="text">Six Jalapenos stuffed with cheese and served with salsa for dipping</span><i class="lead"></i><span class="price">$8.95</span></div>
    <div class="name">Quesadilla</div>
    <div class="row"><span class="text">Sautéed peppers, onions and cheese wrapped in a crispy tortilla shell. Served with salsa and sour cream. Add chicken or beef for</span><i class="lead"></i><span class="price">8.95</span></div>
    <div class="name">Poutine</div>
    <div class="row"><span class="text">This classic Canadian treat will surely be delicious</span><i class="lead"></i><span class="price">$6.95</span></div>
    <div class="name">Newfoundland Fries</div>
    <div class="row"><span class="text">Like the classic Canadian Poutine but with a dash of seasoned ground beef</span><i class="lead"></i><span class="price">$7.95</span></div>
    <div class="name">Mini Beef Tacos</div>
    <div class="row"><span class="text">Shredded beef and green chili in a crispy corn tortilla. Served with salsa</span><i class="lead"></i><span class="price">$8.95</span></div>
    <div class="name">Onion Rings</div>
    <div class="row"><span class="text">Onion rings coated with batter and fried with a crisp. Served with ranch dressing</span><i class="lead"></i><span class="price">$6.95</span></div>
    <div class="name">Potato Skins</div>
    <div class="row"><span class="text">Half dozen baked potato wedges topped with real bacon bits, green onions and mozzarella cheese. Served with sour cream</span><i class="lead"></i><span class="price">$8.95</span></div>
    <div class="name">Mushroom Caps</div>
    <div class="row"><span class="text">Stuffed with crap meat and cream cheese, topped off with melted mozzarella cheese and served with garlic toast</span><i class="lead"></i><span class="price">$9.95</span></div>
    <div class="name">Popcorn Shrimp</div>
    <div class="row"><span class="text">8 oz. of breaded shrimp deep-fried until golden and served with cocktail sauce</span><i class="lead"></i><span class="price">$8.95</span></div>
    <div class="name">Mozza Sticks</div>
    <div class="row"><span class="text">Half dozen delicious deep-fried mozzarella sticks coated with cheese and served with ranch dressing</span><i class="lead"></i><span class="price">$8.95</span></div>
    <div class="name">Tempura Butterfly Shrimp</div>
    <div class="row"><span class="text">Jumbo sized shrimp in mouthwatering tempura batter</span><i class="lead"></i><span class="price">$10.95</span></div>
    <div class="name">Tempura Coconut Shrimp</div>
    <div class="row"><span class="text">Jumbo sized shrimp in mouthwatering tempura batter</span><i class="lead"></i><span class="price">$10.95</span></div>
    <div class="name">Breaded Calamari Rings</div>
    <div class="row"><span class="text">Squid rings coated in batter and deep-fried until golden. Served with dressing</span><i class="lead"></i><span class="price">$9.95</span></div>
    <div class="name">Vegetable Spring Rolls</div>
    <div class="row"><span class="text">Six delicious vegetable rolls. Served with plum sauce</span><i class="lead"></i><span class="price">$6.95</span></div>
    <div class="name">Thai Chicken Bites</div>
    <div class="row"><span class="text">8 oz. of crispy chicken tenders tossed in sweet and hot chili sauce</span><i class="lead"></i><span class="price">$8.95</span></div>
    <div class="name">TZ's Natural Cut Chips</div>
    <div class="row"><span class="text">They taste awesome as it is and even better with spicy seasoning. A must try</span><i class="lead"></i><span class="price">$6.95</span></div>
    <div class="name">Torpedo Shrimps</div>
    <div class="row"><span class="text">Deep fried until golden</span><i class="lead"></i><span class="price">$10.95</span></div>
  </section>

  <section class="panel panel--right">
    <h2 class="title">Favourities</h2>
    <div class="name">Hot Beef Sandwich</div>
    <div class="row"><span class="text">Shaved meat piled high on bread and smothered in gravy</span><i class="lead"></i><span class="price">$13.95</span></div>
    <div class="name">Hot Turkey Sandwich</div>
    <div class="row"><span class="text">Shaved meat piled high on bread and smothered in gravy</span><i class="lead"></i><span class="price">$13.95</span></div>
    <div class="name">Hot Hamburger Sandwich</div>
    <div class="row"><span class="text">This is an all time favorite at TZ's. Home made beef patty on bread and smothered with gravy</span><i class="lead"></i><span class="price">$13.95</span></div>
    <div class="name">Blackened Salmon</div>
    <div class="row"><span class="text">Grilled blackened chicken seasoned with our blackened spice</span><i class="lead"></i><span class="price">$15.95</span></div>
    <div class="name">Pork Chop</div>
    <div class="row"><span class="text">Grilled pork chips topped with sautéed onions and served with applesauce</span><i class="lead"></i><span class="price">$13.95</span></div>
    <div class="name">Liver and Onion</div>
    <div class="row"><span class="text">Tender beef liver grilled to perfection topped with sautéed onions and smothered in gravy</span><i class="lead"></i><span class="price">$13.95</span></div>
    <div class="name">Chicken Parmesan</div>
    <div class="row"><span class="text">A breaded chicken breast covered in meat sauce and melted mozzarella cheese</span><i class="lead"></i><span class="price">$14.95</span></div>
    <div class="name">Veal Parmesan</div>
    <div class="row"><span class="text">A breaded veal cutlet covered in meat sauce and melted mozzarella cheese</span><i class="lead"></i><span class="price">$14.95</span></div>
    <div class="name">Fish and Chips</div>
    <div class="row"><span class="text">Two pieces of cod dipped in our homemade beer batter. Served with tartar sauce</span><i class="lead"></i><span class="price">$12.95</span></div>
    <div class="name">Half BBQ Chicken</div>
    <div class="row"><span class="text">Our oven roasted chicken is a must try</span><i class="lead"></i><span class="price">$13.95</span></div>
    <div class="name">Chicken Fingers</div>
    <div class="row"><span class="text">Breaded chicken fingers deep-fried golden served with plum sauce</span><i class="lead"></i><span class="price">$12.50</span></div>
    <div class="name">Rack of Back Ribs</div>
    <div class="row"><span class="text">Tender back of baby back ribs covered in a tangy BBQ sauce</span><i class="lead"></i><span class="price">$19.95</span></div>
    <div class="name">Chicken Bowl</div>
    <div class="row"><span class="text">Fresh garden vegetable stir-fried with chicken in honey garlic sauce. Served on rice or noodles</span><i class="lead"></i><span class="price">$12.95</span></div>
    <div class="name">Seafood Bowl</div>
    <div class="row"><span class="text">Fresh garden vegetable stir-fried with shrimp and scallop in honey garlic sauce. Served on rice or noodles</span><i class="lead"></i><span class="price">$12.95</span></div>
    <h3 class="subtitle">Gourmet Burger</h3>
    <div class="name">House Burger</div>
    <div class="row"><span class="text">6 oz. Alberta beef topped with cheddar cheese, lettuce, tomato and bacon</span><i class="lead"></i><span class="price">$10.95</span></div>
    <div class="name">Blackened Chicken Burger</div>
    <div class="row"><span class="text">6 oz. charbroiled chicken breast topped with bacon and cheese. Hot and spicy</span><i class="lead"></i><span class="price">$10.95</span></div>
    <div class="name">Prime Rib Burger</div>
    <div class="row"><span class="text">Mouthwatering prime rib patty served cheddar cheese, lettuce, tomato and bacon</span><i class="lead"></i><span class="price">$11.95</span></div>
    <div class="name">Chicken Club Burger</div>
    <div class="row"><span class="text">Grilled chicken breasts topped with cheddar cheese, bacon, lettuce, tomato and mayonnaise</span><i class="lead"></i><span class="price">$10.95</span></div>
    <div class="name">Lotza Mushroom Burger</div>
    <div class="row"><span class="text">6 oz. Alberta beef patty topped with mozzarella cheese, bacon and loads of mushrooms</span><i class="lead"></i><span class="price">$10.95</span></div>
    <div class="name">Crispy Chicken Burger</div>
    <div class="row"><span class="text">Breaded chicken breast deep-fried golden with cheddar cheese, lettuce, tomato and mayonnaise</span><i class="lead"></i><span class="price">$11.95</span></div>
    <h3 class="subtitle">Desserts</h3>
    <div class="row"><span class="text">Lemon Meringue Pie</span><i class="lead"></i><span class="price">$5.95</span></div>
    <div class="row"><span class="text">Apple Pie</span><i class="lead"></i><span class="price">$5.95</span></div>
    <div class="row"><span class="text">Coconut Cream Pie</span><i class="lead"></i><span class="price">$5.95</span></div>
    <div class="row"><span class="text">Cheesecake</span><i class="lead"></i><span class="price">$6.95</span></div>
    <div class="row"><span class="text">Blueberry Pie</span><i class="lead"></i><span class="price">$5.95</span></div>
    <div class="gap"></div>
    <div class="row"><span class="text">355mL Canned Pop</span><i class="lead"></i><span class="price">$1.99</span></div>
    <div class="row"><span class="text">2.0L Bottled Pop</span><i class="lead"></i><span class="price">$3.49</span></div>
  </section>
</main>

<div class="labels">
  <span style="left:100px">Left Panel</span>
  <span style="left:510px">Middle Panel</span>
  <span style="left:883px">Inside Right Panel</span>
</div>
</body>
</html>
```